Google Form Graphic to suit our Brand and industry

Create a graphic / image for us to put at the top of our client enquiry google form.
The image will be a section of an architectural home with our branding over the top. Preferably translucent.
The image must suit the shape of the google forms image, which is an elongated rectangle
#003d5d - brand colour

Target Market(s)

residential home owners, high end architectural homes

Industry/Entity Type

Residential construction

Colors
0054AA
0677BA
7BADD7
CADEEF
E8F1F8

Requirements
Must have
• our branding and a photo of an architectural home in the background

```html
<!DOCTYPE html>
<html lang="en">
<head>
<meta charset="utf-8">
<title>Vela Build – Enquiry Form Header</title>
<link href="https://fonts.googleapis.com/css2?family=Montserrat:wght@600&display=swap" rel="stylesheet">
<style>
  :root {
    --brand-navy: #063d5d;
    --page-bg: #f7f7f7;
    --sky-top: #b9cada;
    --sky-low: #dfe6ee;
    --glass: #8fa3b4;
    --wood: #d1a55e;
    --wood-deep: #6e5231;
    --foliage: #4a6634;
    --white: #ffffff;
  }
  html, body {
    margin: 0;
    padding: 0;
    width: 1200px;
    height: 892px;
    overflow: hidden;
    background: var(--page-bg);
  }
  .form-header {
    position: absolute;
    left: 221px;
    top: 354px;
    width: 759px;
    height: 183px;
    overflow: hidden;
  }
  .home-photo {
    position: absolute;
    inset: 0;
    background:
      linear-gradient(90deg, var(--foliage) 0%, rgba(74,102,52,0.7) 8%, rgba(74,102,52,0) 18%),
      radial-gradient(ellipse 260px 120px at 330px 150px, rgba(209,165,94,0.95) 0%, rgba(209,165,94,0.55) 55%, rgba(209,165,94,0) 100%),
      linear-gradient(180deg, rgba(110,82,49,0) 70%, rgba(60,50,40,0.55) 100%),
      linear-gradient(180deg, var(--sky-top) 0%, var(--sky-low) 35%, var(--glass) 62%, var(--wood-deep) 100%);
  }
  .brand-panel {
    position: absolute;
    inset: 0;
  }
  .brand-name,
  .brand-line {
    position: absolute;
    margin: 0;
    font-family: "Montserrat", sans-serif;
    font-weight: 600;
    white-space: nowrap;
    transform: translateY(-50%);
  }
  .brand-name {
    left: 550px;
    top: 92px;
    width: 94px;
    text-align: center;
    font-size: 20px;
    letter-spacing: 7px;
    text-indent: 7px;
    color: var(--brand-navy);
  }
  .brand-line {
    left: 666px;
    top: 92px;
    font-size: 8px;
    letter-spacing: 4px;
    color: var(--white);
  }
</style>
</head>
<body>
  <header class="form-header">
    <div class="home-photo" role="img" aria-label="Photo of an architectural home with a glass gable over warm timber slats, a dark flat-roofed wing and a tree at the left, under an evening sky"></div>
    <svg class="brand-panel" width="759" height="183" viewBox="0 0 759 183" aria-hidden="true">
      <g fill="var(--brand-navy)">
        <polygon points="534,0 759,0 759,183 530,183 580,160 580,22"/>
        <circle cx="580" cy="93" r="71"/>
      </g>
      <circle cx="597" cy="92" r="54" fill="var(--white)"/>
    </svg>
    <p class="brand-name">VELA</p>
    <p class="brand-line">BUILD</p>
  </header>
</body>
</html>
```